Miel du Matin Immerse in the enchanting flavors of France at Miel du Matin

A menu that is French in style with the Eiffel Tower. A elegant menu that is in rich blue with red or gold trimmings, we are a French Bakey and Cafe

Target Market(s)

30 to 55 people

Industry/Entity Type

Restaurant

Font styles to use
Decorative

Colors
0054AA
0677BA
7BADD7
CADEEF
E8F1F8
EB3D1F
EC4F4E
F09395
F8D3D4
FCEDEE

Requirements
Must have
• the attachment "My Brunch Specials" is the Menu I want you to create, it has all the text, "My Brunch Special Complete" is a word version. The menu size should be 4 1/4 wide by 14 inches long 2 Sided. must have our logo at the top , Make the font larger, because our biggest complaint about our menu is it is hard to read
Nice to have
• I would love to incorporate the Eiffel Tower as a silhouette in the background
Should not have
• I do not want too many pictures or small print

```html
<!DOCTYPE html>
<html lang="en">
<head>
<meta charset="utf-8">
<title>Miel du Matin — Brunch &amp; Drink Specials</title>
<link rel="stylesheet" href="https://fonts.googleapis.com/css2?family=Yesteryear&family=Zilla+Slab:wght@700&family=Lora:wght@400;500&display=swap">
<style>
  :root {
    --blue-deep: #0054AA;
    --blue: #0677BA;
    --blue-soft: #7BADD7;
    --blue-pale: #CADEEF;
    --blue-mist: #E8F1F8;
    --red: #EB3D1F;
    --red-soft: #F09395;
    --ink: #3f3f3f;
    --navy: #1d2238;
    --stage: #dcdcdc;
  }
  * { margin: 0; padding: 0; box-sizing: border-box; }
  html, body { width: 913px; height: 1200px; overflow: hidden; }
  body { background: var(--stage); position: relative; font-family: "Lora", Georgia, serif; }

  .menu-side {
    position: absolute; top: 104px; width: 343px; height: 992px;
    background: #fff; box-shadow: 2px 3px 6px rgba(0,0,0,.22); overflow: hidden;
  }
  .menu-side--brunch { left: 99px; }
  .menu-side--drinks { left: 471px; }

  .wash {
    position: absolute; left: 0; top: 0; width: 343px; height: 90px;
    background: linear-gradient(180deg, var(--blue-pale) 0%, var(--blue-mist) 55%, rgba(255,255,255,0) 100%);
    opacity: .85;
  }
  .corner-ornament {
    position: absolute; left: 20px; top: 17px; width: 79px; height: 79px;
    background: linear-gradient(135deg, var(--red-soft), rgba(240,147,149,.25));
    opacity: .55;
  }
  .brand {
    position: absolute; left: 0; top: 84px; width: 343px; text-align: center;
    font-family: "Lora", Georgia, serif; font-weight: 500; font-size: 12px;
    letter-spacing: 5px; color: var(--navy); text-transform: uppercase;
  }
  .brand-mark {
    position: absolute; left: 159px; top: 30px; width: 26px; height: 26px;
    background: var(--navy);
  }
  .frame { position: absolute; left: 0; top: 0; width: 343px; height: 992px; }
  .flourish {
    position: absolute; left: 289px; top: 271px; width: 52px; height: 247px;
    background: linear-gradient(180deg, rgba(235,61,31,.15), rgba(235,61,31,.45), rgba(235,61,31,.15));
    border-radius: 26px;
  }
  .tower {
    position: absolute; left: 0; top: 711px; width: 85px; height: 281px;
    background: linear-gradient(180deg, rgba(235,61,31,.15), rgba(235,61,31,.55));
    clip-path: polygon(46% 0, 54% 0, 62% 40%, 100% 100%, 0 100%, 0 30%, 38% 40%);
  }

  .section-title {
    position: absolute; left: 0; width: 343px; text-align: center;
    font-family: "Yesteryear", "Brush Script MT", cursive; color: var(--blue); font-weight: 400;
    line-height: 1; white-space: nowrap;
  }
  .section-title--main { top: 112px; font-size: 40px; }
  .section-title--latte { top: 658px; font-size: 36px; }

  .dish { position: absolute; left: 47px; width: 249px; text-align: center; }
  .dish-name {
    font-family: "Zilla Slab", Georgia, serif; font-weight: 700; font-size: 14.5px;
    color: var(--blue); line-height: 16px; margin-bottom: 5px; white-space: nowrap;
  }
  .dish-desc { font-size: 8.1px; line-height: 9.8px; color: var(--ink); }
</style>
</head>
<body>

<section class="menu-side menu-side--brunch" aria-label="Brunch specials">
  <div class="wash" role="img" aria-label="Soft blue watercolour wash"></div>
  <div class="corner-ornament" role="img" aria-label="Red filigree corner ornament"></div>
  <span class="brand-mark"></span>
  <p class="brand">Miel du Matin</p>

  <svg class="frame" viewBox="0 0 343 992" aria-hidden="true">
    <g stroke="var(--red)" stroke-width="1" fill="none">
      <path d="M21 711 V134 H36"/>
      <path d="M310 134 H321 V260"/>
      <path d="M321 521 V967 H77"/>
    </g>
    <g fill="var(--red)">
      <path d="M40 130 l5 4 -5 4 -5 -4z"/>
      <path d="M305 130 l5 4 -5 4 -5 -4z"/>
    </g>
  </svg>
  <div class="flourish" role="img" aria-label="Red scroll flourish"></div>
  <div class="tower" role="img" aria-label="Red line drawing of the Eiffel Tower"></div>

  <h1 class="section-title section-title--main">Brunch Specials</h1>

  <article class="dish" style="top:178px">
    <h2 class="dish-name">Ratatouille &amp; Eggs $18</h2>
    <p class="dish-desc">Experience the essence of Provence with our Ratatouille, a vibrant medley of roasted squash, peppers, tomatoes, eggplant, infused with fragrant fresh herbs. Served with two perfectly poached eggs, and your choice of flavorful andouille sausage or crispy bacon. Accompanied by a side of crusty baguette. It's a hearty dish that celebrates the flavors of the Mediterranean countryside.</p>
  </article>
  <article class="dish" style="top:302px">
    <h2 class="dish-name">Le Grande Breakfast $15</h2>
    <p class="dish-desc">Experience the essence of Provence with our Ratatouille, a vibrant medley of roasted squash, peppers, tomatoes, eggplant, infused with fragrant fresh herbs. Served with two perfectly poached eggs, and your choice of flavorful andouille sausage or crispy bacon. Accompanied by a side of crusty baguette. It's a hearty dish that celebrates the flavors of the Mediterranean countryside.</p>
  </article>
  <article class="dish" style="top:426px">
    <h2 class="dish-name">Smoked Salmon Tartine $14</h2>
    <p class="dish-desc">Delight in the luxurious flavors of our Smoked Salmon Tartine, a culinary masterpiece that elevates breakfast to new heights. Indulge in truffled scrambled eggs nestled atop smoked salmon, adorned with tangy pickled red onions, briny caper berries, crisp cucumber, juicy tomato, and peppery arugula. All artfully arranged on multigrain bread generously spread with herb-infused cream cheese.</p>
  </article>
  <article class="dish" style="top:550px">
    <h2 class="dish-name">Le Benedict Salmon $14</h2>
    <p class="dish-desc">Savor the classic elegance of Eggs Benedict, featuring two perfectly poached eggs nestled on toasted English muffins, with luscious smoked salmon and ripe tomato slices crowned with a velvety lemon-infused Hollandaise sauce. A timeless brunch delight crafted to perfection.</p>
  </article>
  <article class="dish" style="top:654px">
    <h2 class="dish-name">Salmon Atlantique $14</h2>
    <p class="dish-desc">Enjoy a bed of crisp mixed greens adorned with delicate smoked salmon, sweet golden raisins, creamy goat cheese, and crunchy walnuts. All dressed in a tantalizing balsamic vinaigrette that ties the elements together perfectly.</p>
  </article>
  <article class="dish" style="top:751px">
    <h2 class="dish-name">Beef Bourguignon $18</h2>
    <p class="dish-desc">Indulge in our rich and comforting flavors of savory, tender beef slowly braised in red wine, creating a luscious sauce that envelops pearl onions, carrots, and mushrooms in a symphony of flavors. Served alongside buttered egg noodles. It's a hearty and soul-warming meal that promises pure culinary bliss.</p>
  </article>
  <article class="dish" style="top:860px">
    <h2 class="dish-name">Tourte Au Poulet $15</h2>
    <p class="dish-desc">Discover the indulgent flavors of our Tourte au Poulet, a savory delight that marries tender marinated chicken with the richness of Swiss cheese and the sweetness of onions, all encased in layers of flaky pastry. Topped with a savory mushroom medley and decadent bechamel sauce. A true comfort classic to delight your senses.</p>
  </article>
</section>

<section class="menu-side menu-side--drinks" aria-label="Drink specials and lattes">
  <div class="wash" role="img" aria-label="Soft blue watercolour wash"></div>
  <div class="corner-ornament" role="img" aria-label="Red filigree corner ornament"></div>
  <span class="brand-mark"></span>
  <p class="brand">Miel du Matin</p>

  <svg class="frame" viewBox="0 0 343 992" aria-hidden="true">
    <g stroke="var(--red)" stroke-width="1" fill="none">
      <path d="M36 134 H21 V649 H321 V521"/>
      <path d="M310 134 H321 V260"/>
      <path d="M21 711 V677 H110"/>
      <path d="M230 677 H321 V967 H77"/>
    </g>
    <g fill="var(--red)">
      <path d="M40 130 l5 4 -5 4 -5 -4z"/>
      <path d="M305 130 l5 4 -5 4 -5 -4z"/>
      <path d="M110 673 l5 4 -5 4 -5 -4z"/>
      <path d="M230 673 l5 4 -5 4 -5 -4z"/>
    </g>
  </svg>
  <div class="flourish" role="img" aria-label="Red scroll flourish"></div>
  <div class="tower" role="img" aria-label="Red line drawing of the Eiffel Tower"></div>

  <h1 class="section-title section-title--main">Drink Specials</h1>

  <article class="dish" style="top:178px">
    <h2 class="dish-name">Bottomless Mimosa $18</h2>
    <p class="dish-desc">Embark on an endless journey of delight with our Bottomless Mimosa, featuring Valmont champagne, infusing each sip with a sparkling ensation. Tailor your experience with your preferred flavor profile - opt for the timeless twist of classic orange juice or tangy cranberry juice for a refreshing zing. Continuously poured to ensure your glass is always full.</p>
  </article>
  <article class="dish" style="top:274px">
    <h2 class="dish-name">Apple Cider Mimosa $9</h2>
    <p class="dish-desc">A delightful twist on the classic mimosa. Crafted with champagne and crisp apple cider. To elevate the experience, we adorn the glass with a caramel rim dipped in brown sugar, adding a touch of indulgent sweetness to every sip.</p>
  </article>
  <article class="dish" style="top:347px">
    <h2 class="dish-name">Blood Orange or Pineapple Spritz $12</h2>
    <p class="dish-desc">Introducing our vibrant spritz cocktail, a tantalizing blend of Harlow &amp; Pine's premium Vesna Vodka, sweet vermouth, and a touch of sweetness from a carefully muddled sugar cube. This effervescent libation reaches new heights with the addition of bubbly Clairsource, your choice of either Blood Orange or Pineapple syrup injects a burst of fruity allure into every sip.</p>
  </article>
  <article class="dish" style="top:452px">
    <h2 class="dish-name">Peach Bellini $9</h2>
    <p class="dish-desc">Try our perfectly balanced Peach Bellini with each sip you capture the crispness of champagne with the irresistible sweetness of peach. It's a sublime fusion of sophistication and sweetness.</p>
  </article>
  <article class="dish" style="top:517px">
    <h2 class="dish-name">Espresso Martini $10</h2>
    <p class="dish-desc">Our Espresso Martini is a decadent blend of bold espresso, rich chocolate martini, and luxurious Belcour chocolate syrup. It's the ultimate indulgence for coffee and chocolate lovers alike.</p>
  </article>
  <article class="dish" style="top:583px">
    <h2 class="dish-name">Kir Royale $10</h2>
    <p class="dish-desc">Our Kir Royale is a delightful fusion of the crisp, sparkling champagne bubbles and the sweet sophistication of black currant. a luxurious and indulgent drink that's perfect for any occasion.</p>
  </article>

  <h1 class="section-title section-title--latte">Latte</h1>

  <article class="dish" style="top:702px">
    <h2 class="dish-name">Truffle Latte $6</h2>
    <p class="dish-desc">We start with rich Belcour chocolate, known for its velvety smoothness and intense flavor. Then, we add a drizzle of salted caramel, adding a perfect balance of sweetness and a hint of savory richness. Finally, we combine this delightful blend with perfectly steamed milk to create a creamy and indulgent latte that will satisfy even the most discerning palate.</p>
  </article>
  <article class="dish" style="top:792px">
    <h2 class="dish-name">Napoleon Latte $6</h2>
    <p class="dish-desc">We start with our rich espresso, renowned for its bold and robust character. Then, we add a luscious combination of hazelnut and vanilla syrup, creating a symphony of sweetness and nutty richness. As the final touch, we crown this masterpiece with the velvety smoothness of perfectly steamed milk.</p>
  </article>
  <article class="dish" style="top:872px">
    <h2 class="dish-name">Chai Latte $6</h2>
    <p class="dish-desc">Our robust chai tea concentrate, infused with a symphony of cinnamon, cardamom, cloves, and ginger, sets the stage for a journey of aromatic delight. Paired with velvety steamed milk, each sip offers a harmonious blend of bold spices and creamy richness. Topped with a sprinkle of cinnamon, it's the perfect finishing touch to this comforting treat.</p>
  </article>
</section>

</body>
</html>
```